Redesign of Plastic Surgeon Website to fully responsive / modern feel

Hi

Our current website is out of date www.harbourlinecosmetic.org

We want a fresh / modern looking design
Needs to be fully responsive design that works extremely well on ipad and mobile device

Would like design for both full screen website and mobile

Have listed a few websites of other plastic surgeons we like
http://www.reformclinicdaily.com/
http://www.peterholtbymd.com/
http://www.corvanbeauty.com/
http://www.tidewellcontouring.com/

Menu needs to include
1. About Us
2. Procedures (see current website for example)
3. News
4. Patient Resources
5. Contact Us

We are flexible with colours / images / layout

I have uploaded a document that has some content - the face pages content is completed only

some of the procedures can have content upwards of 4000 words - total website can be large with over 40,000 words
Updates

Target Market(s)

Mainly women 20-60 85% of practice
Some men 15%

Industry/Entity Type

Plastic Surgery

Number of Pages Required

5+ page

Requirements
Must have
• We need designs for
• Homepage
• Internal pages
• 1. Landing pages for breast / body / face / non surgical main pages
• 2. Procedure pages for individual pages under each section - eg breast augmentation
• 3. About us pages - like meet the doctor, our staff, clinics
• 4. Contact page
• 5. Blog / News page
Nice to have
• See our list of websites for examples of designs we like
• Like full screen design with nice hero image
• Needs to have good to call to action messages on home page like
• Specials, procedure of the month, etc

```html
<!DOCTYPE html>
<html lang="en">
<head>
<meta charset="utf-8">
<title>About Us – Harbourline Cosmetic Institute</title>
<link href="https://fonts.googleapis.com/css2?family=Raleway:wght@300;400&family=PT+Sans:wght@400;700&display=swap" rel="stylesheet">
<style>
:root{
  --orange:#d0612a;
  --amber:#d6852f;
  --grey-text:#8a8a8a;
  --dark-text:#3b3b3b;
  --side-grey:#a0a0a0;
  --band-light:#f2f2f2;
  --footer:#2a2624;
  --sand:#cdbf98;
  --mint:#a9e4d8;
  --olive:#6b5f45;
}
*{margin:0;padding:0;box-sizing:border-box}
html,body{width:923px;height:1200px;overflow:hidden;background:#fff}
body{position:relative;font-family:"PT Sans",sans-serif;color:var(--grey-text)}
.abs{position:absolute}

/* header */
.site-header{left:0;top:0;width:923px;height:94px;background:#fff;box-shadow:0 2px 4px rgba(0,0,0,.08);z-index:2}
.brand-box{left:78px;top:0;width:284px;height:94px;background:#fff;box-shadow:0 0 6px rgba(0,0,0,.15);display:flex;align-items:center;justify-content:center;gap:8px}
.brand-mark{width:14px;height:14px;border-radius:50%;background:var(--amber)}
.brand-name{font-family:"Raleway",sans-serif;font-weight:400;font-size:17px;color:var(--amber);line-height:1.1}
.call-box{left:570px;top:0;width:285px;height:33px;background:#d9d9d9;display:flex;align-items:center;padding-left:14px;gap:8px;font-size:9.5px;color:#fff;letter-spacing:.2px}
.call-box b{color:var(--amber);font-size:15px;font-weight:700;letter-spacing:.5px}
.main-nav{left:402px;top:68px;display:flex;gap:24px;font-size:9px;color:#333;text-transform:uppercase}
.main-nav span.active{color:var(--amber)}
.caret{display:inline-block;border:3px solid transparent;border-top:4px solid currentColor;margin-left:4px;vertical-align:-1px}

/* title band */
.title-band{left:0;top:94px;width:923px;height:76px;background:linear-gradient(100deg,#f3f3f3 60%,#fafafa 80%,#eeeeee)}
.page-title{left:66px;top:116px;font-family:"Raleway",sans-serif;font-weight:300;font-size:26px;color:#444}
.crumbs{left:67px;top:151px;font-size:7.5px;font-style:italic;color:#b5a98c}
.crumbs span{color:#8d8d8d}
.rule-bars{left:0;top:170px;width:923px;height:5px;display:flex}
.rule-bars i{flex:1}

/* sidebar */
.side-nav{left:66px;top:202px;width:182px}
.side-nav div{height:30px;line-height:30px;padding-left:6px;font-size:8.8px;font-weight:700;color:#fff;text-transform:uppercase;background:var(--side-grey);border-bottom:1px solid #c4c4c4;letter-spacing:.3px}
.side-nav div.current{background:var(--orange)}

/* content */
.content{left:269px;top:200px;width:582px}
.content h2{font-family:"Raleway",sans-serif;font-weight:400;font-size:20px;color:#333;margin-bottom:4px}
.content p{font-size:8.4px;line-height:16.5px;margin-bottom:12px}
.values{list-style:none}
.values li{position:relative;padding-left:16px;font-size:8.4px;line-height:16.5px;margin-bottom:7px}
.values li::before{content:"";position:absolute;left:1px;top:5px;width:6px;height:6px;border-radius:50%;background:var(--orange)}
.values b{color:var(--orange);font-weight:700}

/* affiliations */
.affil{left:0;top:618px;width:923px;height:148px;background:linear-gradient(180deg,#eeebe6,#f1efea 50%,#e6e0d6);display:flex;align-items:center;justify-content:space-between;padding:0 66px}
.badge{background:#b9bcc2;opacity:.85}

/* tiles */
.tiles{left:0;top:766px;width:923px;height:185px;display:flex}
.tile{flex:1;position:relative;display:flex;align-items:center;justify-content:center;font-weight:700;font-size:16px;color:#fff;text-shadow:0 1px 3px rgba(0,0,0,.4)}
.tile-face{background:linear-gradient(160deg,#3a3430,#9e7e6a 55%,#4a3c34)}
.tile-breast{background:linear-gradient(150deg,#4d3a30,#8c6a58 50%,#3b2c25)}
.tile-body{background:linear-gradient(180deg,#3b2e26,#a27b62 55%,#6a4d3c)}
.tile-nonsurg{background:linear-gradient(120deg,#6b4a37,#d6ad92 50%,#ead9cd)}

/* footer */
.site-footer{left:0;top:951px;width:923px;height:214px;background:var(--footer)}
.foot-h{font-family:"Raleway",sans-serif;font-weight:400;font-size:16.5px;color:#eee}
.sitemap{left:66px;top:990px}
.sitemap ul{list-style:none;margin-top:14px;font-size:10.5px;color:#eee;line-height:16.2px}
.news{left:200px;top:990px;width:280px}
.news-thumb{left:201px;top:1023px;width:83px;height:65px;background:linear-gradient(135deg,#e7c4ad,#c99b83)}
.news-title{left:293px;top:1024px;font-size:10px;color:var(--amber)}
.news-text{left:296px;top:1041px;width:178px;font-size:9.4px;line-height:11.5px;color:#eee;text-align:justify}
.view-all{left:389px;top:1105px;width:84px;height:23px;background:var(--amber);color:#fff;font-size:8.5px;display:flex;align-items:center;justify-content:center}
.clinic{left:513px;top:990px}
.clinic-cols{left:513px;top:1023px;display:flex;gap:16px;font-size:8.6px;color:#eee;line-height:11.3px}
.clinic-cols strong{display:block;font-weight:400;font-size:11.5px;color:var(--amber);line-height:14px}
.copy{left:0;top:1165px;width:923px;height:35px;background:var(--amber);display:flex;align-items:center;justify-content:center;font-family:"Raleway",sans-serif;font-size:7.5px;color:#fff}
</style>
</head>
<body>

<header class="abs site-header">
  <div class="abs brand-box"><span class="brand-mark"></span><span class="brand-name">Harbourline Cosmetic Institute</span></div>
  <div class="abs call-box">
    <svg width="12" height="14" viewBox="0 0 12 14"><path d="M3 1 L5 4 L3.5 5.5 C4.5 8 6 9.5 8.5 10.5 L10 9 L12 11.5 L10 13.5 C5 13 1 8 0.5 3 Z" fill="#fff"/></svg>
    <span>CALL FOR APPOINTMENTS : <b>02 9000 4821</b></span>
  </div>
  <nav class="abs main-nav">
    <span class="active">About Us<i class="caret"></i></span>
    <span>Procedures<i class="caret"></i></span>
    <span>Patient Resources<i class="caret"></i></span>
    <span>News / Blogs</span>
    <span>Contact Us</span>
  </nav>
</header>

<div class="abs title-band"></div>
<h1 class="abs page-title">About Us</h1>
<div class="abs crumbs">About Us &gt; <span>Our Philosophy &amp; Values</span></div>
<div class="abs rule-bars"><i style="background:var(--sand)"></i><i style="background:var(--mint)"></i><i style="background:var(--orange)"></i><i style="background:var(--olive)"></i></div>

<aside class="abs side-nav">
  <div class="current">Our Philosophy and Values</div>
  <div>Meet Dr Whitcombe</div>
  <div>Our Staff</div>
  <div>Locations</div>
</aside>

<main class="abs content">
  <h2>Our Vision</h2>
  <p>With advanced techniques, expertise and constant client feedback, we aim to remain at the forefront of surgical rejuvenation and deliver outstanding results for clients who value experience, empathy and quality outcomes.</p>
  <h2>Our Mission</h2>
  <p>To provide exceptional quality of service in plastic and cosmetic surgery, and improve the appearance, wellbeing and self confidence of clients entrusting us with their care.</p>
  <h2>Our Values</h2>
  <ul class="values">
    <li><b>Integrity</b> – We aim to impress with education rather than promotion. All photographs on this website are of Dr Whitcombe’s own clients, and are not enhanced or digitally embellished. The outcomes of surgery shown are true representations of our results.</li>
    <li><b>Accessibility</b> – Peace of mind with 24/7 service. All clients have direct access to Dr Whitcombe and his team before, during and after surgical procedures.</li>
    <li><b>Empathy</b> – We treat clients with absolute respect. You can feel confident sharing your choices, opinions and feelings with our sincere, mature and non-judgemental staff.</li>
    <li><b>Privacy</b> – Absolute discretion. Your details and treatment history are kept in strict confidence at all times.</li>
    <li><b>Feedback</b> – Your thoughts and feelings are important to us. We encourage feedback, comments and suggestions to ensure satisfaction with every aspect of your experience.</li>
    <li><b>Progress</b> – Ongoing professional development ensures all our staff members remain up to date with the latest techniques and operations.</li>
  </ul>
</main>

<section class="abs affil" role="img" aria-label="Professional association membership badges over a soft meadow background">
  <div class="badge" style="width:116px;height:40px;border-radius:4px"></div>
  <div class="badge" style="width:60px;height:60px;border-radius:50%"></div>
  <div class="badge" style="width:150px;height:46px;border-radius:4px"></div>
  <div class="badge" style="width:56px;height:70px;border-radius:4px"></div>
  <div class="badge" style="width:80px;height:56px;border-radius:4px"></div>
  <div class="badge" style="width:116px;height:44px;border-radius:4px"></div>
  <div class="badge" style="width:56px;height:56px;border-radius:50%"></div>
</section>

<section class="abs tiles">
  <div class="tile tile-face" role="img" aria-label="Photo of a smiling mature woman for face procedures">Face</div>
  <div class="tile tile-breast" role="img" aria-label="Photo of a woman's shoulder and chest for breast procedures">Breast</div>
  <div class="tile tile-body" role="img" aria-label="Photo of a bare back for body procedures">Body</div>
  <div class="tile tile-nonsurg" role="img" aria-label="Photo of a young woman with clear skin for non-surgical treatments">Non-Surgical</div>
</section>

<footer class="abs site-footer"></footer>
<div class="abs sitemap">
  <div class="foot-h">Sitemap</div>
  <ul><li>Home</li><li>About Us</li><li>Procedures</li><li>Patient Resources</li><li>News / Blog</li><li>Contact Us</li></ul>
</div>
<div class="abs news"><div class="foot-h">Latest News / Blogs</div></div>
<div class="abs news-thumb" role="img" aria-label="Photo of hands resting on a woman's abdomen"></div>
<div class="abs news-title">Who should have a tummy tuck?</div>
<p class="abs news-text">After giving birth or losing heaps of weight, many women find the shape of their tummy has dramatically changed and, no matter how much cardio ...</p>
<div class="abs view-all">VIEW ALL</div>
<div class="abs clinic"><div class="foot-h">Our Clinic</div></div>
<div class="abs clinic-cols">
  <div><strong>Bayview</strong>210 Cove Parade, Suite 12<br>Bayview, NSW 2104</div>
  <div><strong>Annandale</strong>Level 1<br>47 Larkin Street 2041<br>Tel: 02 9000 4821</div>
  <div><strong>Kotara</strong>5/18 Fernleigh Rd<br>Kotara, NSW 2289</div>
</div>
<div class="abs copy">© Harbourline Cosmetic Institute Dr Ellis Whitcombe Plastic Surgery Sydney Australia 2016</div>

</body>
</html>
```